Q-Rolls Business Card

We are a modern retail clothing store. Established in 1994. I need a presentable card that will amaze vendors when given to them.

Front: Logo in middle
Info Side:

Name: Tomas Velder
Cell: 630-812-4463
Work: 630-917-3384 EXT. 417
Email: Tomas@q-rolls-example.com
Website: www.Q-rolls-example.com

Industry/Entity Type

Business

```html
<!DOCTYPE html>
<html lang="en">
<head>
<meta charset="utf-8">
<title>Q-Rolls Business Card</title>
<link rel="stylesheet" href="https://fonts.googleapis.com/css2?family=Open+Sans:wght@400;600;700&display=swap">
<style>
  :root {
    --backdrop: #4a3222;
    --card-black: #000000;
    --card-yellow: #fbe000;
    --brand-yellow: #f7dc00;
    --ink: #111111;
  }
  * { margin: 0; padding: 0; box-sizing: border-box; }
  html, body {
    width: 1200px;
    height: 1000px;
    overflow: hidden;
    background: var(--backdrop);
    font-family: "Open Sans", Arial, sans-serif;
  }
  .canvas {
    position: relative;
    width: 1200px;
    height: 1000px;
  }
  .card {
    position: absolute;
    left: 290px;
    width: 618px;
    height: 363px;
    border-radius: 14px;
  }
  .card--front {
    top: 124px;
    background: var(--card-black);
  }
  .card--info {
    top: 512px;
    background: var(--card-yellow);
  }
  .brand-name {
    position: absolute;
    font-weight: 600;
    letter-spacing: 1px;
    white-space: nowrap;
  }
  .card--front .brand-name {
    left: 0;
    right: 0;
    top: 140px;
    text-align: center;
    font-size: 66px;
    line-height: 1;
    color: var(--brand-yellow);
  }
  .card--info .brand-name {
    left: 28px;
    top: 34px;
    font-size: 52px;
    line-height: 1;
    color: var(--ink);
  }
  .website {
    position: absolute;
    left: 0;
    right: 0;
    top: 316px;
    text-align: center;
    font-size: 16px;
    font-weight: 700;
    color: var(--brand-yellow);
  }
  .contact {
    position: absolute;
    right: 36px;
    top: 224px;
    text-align: right;
    color: var(--ink);
  }
  .contact__name {
    font-size: 19px;
    font-weight: 700;
    margin-bottom: 24px;
  }
  .contact__line {
    font-size: 15.5px;
    font-weight: 400;
    line-height: 23px;
  }
</style>
</head>
<body>
  <main class="canvas">
    <section class="card card--front">
      <div class="brand-name">Q-ROLLS</div>
      <div class="website">www.Q-rolls-example.com</div>
    </section>
    <section class="card card--info">
      <div class="brand-name">Q-ROLLS</div>
      <div class="contact">
        <div class="contact__name">Tomas Velder</div>
        <div class="contact__line">M: 630-812-4463</div>
        <div class="contact__line">T: 630-917-3384 EXT. 417</div>
        <div class="contact__line">E: Tomas@q-rolls-example.com</div>
      </div>
    </section>
  </main>
</body>
</html>
```